Award-winnning Estate Agent needs a premium version of their 'For Sale' board design

We need a premium option for our 'For Sale' board design. We have a standard board that is attached to this brief, but were are looking to have a premium design version that we will use when selling exclusive properties. Our company name is Harbour Lane Estates and the name for this is exclusive selection is: 'The Harbour Collection'. The design needs to work with our current brand, but have a distinctive PREMIUM feel to it. I have uploaded the barnd guidelines and also some of the exisisting logo variations. We do NOT need a new logo but feel free to play around with colours, fonts, sizes etc. for the sign.

Target Market(s)

Property buyers & house hunters

Industry/Entity Type

Real Estate - Residential Property

Font styles to use
Sans Serif

Requirements
Must have
• A premium fee, must be square design, must be easy to read when driving past the sign
Nice to have
• I'm open ot ideas

```html
<!DOCTYPE html>
<html lang="en">
<head>
<meta charset="utf-8">
<title>Harbour Lane Estates – For Sale board</title>
<link rel="stylesheet" href="https://fonts.googleapis.com/css2?family=Arimo:wght@400;700&display=swap">
<style>
  :root {
    --royal-blue: #0010ee;
    --faint-blue: #2a3bff;
    --gold: #cf9152;
    --gold-text: #b88f5c;
    --gold-band: #a67c45;
    --white: #ffffff;
  }
  * { margin: 0; padding: 0; box-sizing: border-box; }
  html, body { width: 1200px; height: 1200px; overflow: hidden; background: var(--white); }
  body { font-family: "Arimo", Arial, sans-serif; position: relative; }

  .board { position: absolute; inset: 0; }

  .brand-panel {
    position: absolute; left: 34px; top: 34px; width: 1139px; height: 703px;
    background: var(--royal-blue); overflow: hidden;
  }
  .side-flourish {
    position: absolute; top: 0; width: 163px; height: 394px;
    background: linear-gradient(180deg, rgba(42,59,255,0.0), rgba(42,59,255,0.55) 50%, rgba(42,59,255,0.0));
    border-radius: 0 80px 80px 0;
  }
  .side-flourish.left { left: 0; }
  .side-flourish.right { right: 0; border-radius: 80px 0 0 80px; }

  .brand-mark {
    position: absolute; left: 50%; top: 110px; width: 150px; height: 150px;
    margin-left: -75px; background: var(--gold);
  }
  .brand-name {
    position: absolute; left: 0; right: 0; top: 366px;
    text-align: center; color: var(--gold-text);
    font-weight: 700; font-size: 80px; letter-spacing: -1px; line-height: 1;
  }

  .crest-flourish {
    position: absolute; left: 50%; top: 463px; width: 136px; height: 60px;
    margin-left: -68px; background: var(--gold-text); opacity: 0.9;
    border-radius: 60px 60px 10px 10px;
  }
  .rule {
    position: absolute; left: 136px; width: 869px; height: 2px; background: var(--gold-text);
  }
  .rule.upper { top: 532px; }
  .rule.lower { top: 656px; }
  .collection-name {
    position: absolute; left: 0; right: 0; top: 563px;
    text-align: center; color: var(--gold-text);
    font-weight: 400; font-size: 64px; line-height: 1; letter-spacing: 0.5px;
  }

  .sale-band {
    position: absolute; left: 34px; top: 758px; width: 1139px; height: 196px;
    background: var(--gold-band);
    display: flex; align-items: center; justify-content: center;
  }
  .sale-band .sale-label {
    color: var(--white); font-weight: 700; font-size: 184px; line-height: 1;
    letter-spacing: 2px; margin-top: 6px;
  }

  .phone {
    position: absolute; left: 0; right: 0; top: 983px; text-align: center;
    color: var(--royal-blue); font-weight: 700; font-size: 104px; line-height: 1;
    letter-spacing: 1px;
  }
  .website {
    position: absolute; left: 0; right: 0; top: 1104px; text-align: center;
    color: var(--royal-blue); font-weight: 400; font-size: 63px; line-height: 1;
  }
</style>
</head>
<body>
  <main class="board">
    <section class="brand-panel">
      <div class="side-flourish left" role="img" aria-label="Faint decorative scroll flourish"></div>
      <div class="side-flourish right" role="img" aria-label="Faint decorative scroll flourish"></div>

      <div class="brand-mark" aria-hidden="true"></div>
      <h1 class="brand-name">Harbour Lane Estates</h1>

      <div class="crest-flourish" role="img" aria-label="Gold ornamental flourish"></div>
      <div class="rule upper"></div>
      <h2 class="collection-name">THE HARBOUR COLLECTION</h2>
      <div class="rule lower"></div>
    </section>

    <section class="sale-band">
      <span class="sale-label">FOR SALE</span>
    </section>

    <p class="phone">01632 960412</p>
    <p class="website">www.harbourlaneestates.co.uk</p>
  </main>
</body>
</html>
```